Dental Co needs single page print ad

Dental company needs a 1 page ad for trade magazines.
I am uploading an example of what we want (words). We need you to make it look great. It can include people or not.
The uploaded ad isn't there to be copied, just to kind of frame what we are thinking. We are open to any design
One page ad
Size 1)

Trim Size - 8 x 10.5
Bleed Size - 8.25 x 10.75
Live Area - 7 x 10

Size 2)

Trim - 8 x 10.875
Bleed - 8.25 x 11.125
Live Area - 7 x 9.875

BRIX Brand Hex #'s

Orange - ff6319
Teal - 56b1bf
Lt. Teal - aed9da
Blue: #38394B

Target Market(s)

Dentists

Requirements
Must have
• BRIX Logo, pic of the sensor (called VANT)
Use the brand hex colors:
Orange - ff6319
Teal - 56b1bf
Lt. Teal - aed9da
Blue: #38394B

```html
<!DOCTYPE html>
<html lang="en">
<head>
<meta charset="utf-8">
<title>Brix Imaging – VANT Sensor Ad</title>
<link rel="stylesheet" href="https://fonts.googleapis.com/css2?family=Rubik:ital,wght@0,700;1,500;1,700;1,800&family=Open+Sans:ital,wght@1,700&display=swap">
<style>
  :root {
    --orange: #ff6319;
    --teal: #56b1bf;
    --lt-teal: #aed9da;
    --brand-blue: #38394b;
    --navy: #1f2556;
    --footer-navy: #1b2350;
    --white: #ffffff;
    --page: #ffffff;
  }
  * { margin: 0; padding: 0; box-sizing: border-box; }
  html, body {
    width: 1200px; height: 614px; overflow: hidden;
    background: var(--page);
  }
  .ad {
    position: absolute; left: 378px; top: 17px;
    width: 443px; height: 580px; overflow: hidden;
    background: var(--white);
    box-shadow: 0 1px 4px rgba(0,0,0,.18);
    font-family: "Rubik", sans-serif;
  }
  .ad > * { position: absolute; }

  .hero-photo {
    left: 190px; top: 0; width: 253px; height: 240px;
    background: linear-gradient(100deg, #ffffff 0%, #e9e9e9 35%, #c9c9c9 70%, #b5b5b5 100%);
  }
  .brand-name {
    left: 20px; top: 30px;
    font-weight: 700; font-size: 30px; letter-spacing: .5px;
    color: var(--navy); line-height: 1;
  }
  .headline {
    left: 22px; top: 112px; width: 200px;
    font-weight: 800; font-style: italic; font-size: 23px;
    line-height: 22px; color: var(--brand-blue);
  }
  .headline .accent { color: var(--orange); font-size: 28px; }

  .product-band {
    left: 0; top: 240px; width: 443px; height: 87px;
    background: var(--lt-teal);
  }
  .product-name {
    left: 22px; top: 250px;
    font-weight: 700; font-size: 58px; letter-spacing: 1px;
    color: var(--navy); line-height: 1;
  }
  .product-name .accent { color: var(--orange); }

  .lower-panels { left: 0; top: 327px; width: 443px; height: 217px; }

  .price-setup { left: 26px; top: 340px; color: var(--orange); }
  .price-monthly { left: 26px; top: 455px; color: var(--brand-blue); }
  .price-amount {
    font-weight: 800; font-style: italic; font-size: 44px; line-height: 1;
  }
  .price-note {
    margin-top: 4px; font-weight: 500; font-style: italic;
    font-size: 19px; line-height: 18px;
  }
  .price-setup .price-note { color: var(--teal); }

  .sensor-photo {
    left: 250px; top: 250px; width: 165px; height: 180px;
    border-radius: 34px;
    background: radial-gradient(circle at 30% 25%, #5a5f9a 0%, #343a78 45%, #1c2154 100%);
    transform: rotate(-6deg);
    box-shadow: 6px 8px 14px rgba(0,0,0,.35);
  }

  .benefits {
    right: 10px; top: 461px; list-style: none; text-align: right;
    font-family: "Open Sans", sans-serif; font-style: italic; font-weight: 700;
    font-size: 10.5px; line-height: 16.2px; color: var(--white);
  }
  .benefits li::after { content: " \2190"; font-style: normal; }

  .footer {
    left: 0; top: 544px; width: 443px; height: 36px;
    background: var(--footer-navy);
    display: flex; align-items: center; justify-content: center;
    font-weight: 500; font-style: italic; font-size: 15px;
    letter-spacing: 1.6px; color: var(--white);
  }
</style>
</head>
<body>
  <main class="ad">
    <div class="hero-photo" role="img" aria-label="Black and white photo of a woman with orange lips holding a dental sensor near her chin"></div>
    <div class="brand-name">BRIX IMAGING</div>
    <h1 class="headline">A subscription option for intra-oral <span class="accent">sensors</span> is dumb</h1>

    <div class="product-band"></div>
    <div class="product-name">V<span class="accent">A</span>NT</div>

    <svg class="lower-panels" viewBox="0 0 443 217" aria-hidden="true">
      <rect x="0" y="0" width="443" height="121" fill="var(--brand-blue)"/>
      <rect x="0" y="121" width="443" height="96" fill="var(--teal)"/>
      <polygon points="205,217 443,40 443,217" fill="var(--orange)"/>
      <g stroke="var(--white)" stroke-width="1" fill="none">
        <polyline points="225,6 18,6 18,118"/>
        <polyline points="190,125 18,125 18,214"/>
      </g>
    </svg>

    <div class="price-setup">
      <div class="price-amount">$1,999</div>
      <div class="price-note">one-time sign<br>up fee</div>
    </div>
    <div class="price-monthly">
      <div class="price-amount">$139/</div>
      <div class="price-note">mo - cancel<br>anytime</div>
    </div>

    <div class="sensor-photo" role="img" aria-label="Photo of the VANT intra-oral sensor"></div>

    <ul class="benefits">
      <li>Lifetime $0 deductible warranty</li>
      <li>Unlimited support &amp; upgrades</li>
      <li>Direct integration w/all major software</li>
      <li>Affordable enough for every op</li>
      <li>Preserve your capital</li>
    </ul>

    <div class="footer">www.briximaging.com&nbsp;&nbsp;|&nbsp;&nbsp;(555) 014-BRIX</div>
  </main>
</body>
</html>
```